Business Card Design for a Software Startup

We'd like to have a business card design. We already have a logo. Basically what we need is a clean design with name, address, cellphone and phone numbers, e-mail and web site address (front) and a space on the back with our logo with the company name on the right side and some texts on the bottom.
We are a development and consulting company in Brazil with highly qualified team of professionals in Kavra, Lumo and Orbitex development and consulting.

Target Market(s)

CIO, IT managers of mid to big size companies

Industry/Entity Type

Business

```html
<!DOCTYPE html>
<html lang="en">
<head>
<meta charset="utf-8">
<title>VELTRA Business Card – Front and Back</title>
<link rel="stylesheet" href="https://fonts.googleapis.com/css2?family=Josefin+Sans:wght@300;400;600;700&family=Roboto+Condensed:ital,wght@1,400&display=swap">
<style>
  :root {
    --sky: #c9fbfc;
    --page: #ffffff;
    --card-black: #000000;
    --cyan: #12e8f5;
    --cyan-soft: #2fe7ee;
    --azure: #0a8fd0;
    --navy: #0b1a8c;
    --brand-blue: #1740b0;
    --ink-white: #f4f6f8;
    --label-ink: #111111;
  }
  * { margin: 0; padding: 0; box-sizing: border-box; }
  html, body { width: 1200px; height: 1000px; overflow: hidden; }
  body {
    position: relative;
    background: linear-gradient(180deg, var(--sky) 0%, var(--page) 38%, var(--page) 100%);
    font-family: "Josefin Sans", "Century Gothic", sans-serif;
    color: var(--ink-white);
  }
  .card-frame {
    position: absolute;
    border-radius: 26px 14px 26px 14px;
    background: linear-gradient(45deg, var(--cyan) 0%, var(--azure) 50%, var(--navy) 100%);
    box-shadow: 0 14px 14px -10px rgba(0, 0, 0, 0.35);
  }
  .card-face {
    position: absolute;
    background: var(--card-black);
    border-radius: 22px;
    box-shadow: 0 0 6px rgba(255, 255, 255, 0.8);
  }
  .card-front { left: 33px; top: 27px; width: 752px; height: 429px; }
  .card-front .card-face { left: 15px; top: 18px; width: 724px; height: 393px; }
  .card-back { left: 405px; top: 520px; width: 745px; height: 426px; }
  .card-back .card-face { left: 17px; top: 20px; width: 713px; height: 388px; }

  .rule { position: absolute; height: 3px; }
  .rule-cyan-to-navy { background: linear-gradient(90deg, var(--cyan), var(--navy)); }
  .rule-navy-to-cyan { background: linear-gradient(90deg, var(--navy), var(--cyan)); }

  .brand-mark {
    position: absolute;
    border-radius: 18px;
    background: var(--brand-blue);
  }
  .brand-name {
    position: absolute;
    font-weight: 700;
    color: var(--brand-blue);
    line-height: 1;
    white-space: nowrap;
  }

  .contact { position: absolute; left: 395px; width: 350px; text-align: center; white-space: nowrap; }
  .contact-name { top: 106px; font-size: 44px; font-weight: 300; color: var(--cyan-soft); letter-spacing: 1px; }
  .contact-street { top: 168px; font-size: 32px; font-weight: 300; letter-spacing: 1.5px; }
  .contact-phone { font-size: 37px; font-weight: 300; letter-spacing: 1px; }
  .contact-phone .phone-tag { font-size: 20px; font-style: italic; font-weight: 300; color: var(--cyan-soft); letter-spacing: 0; }
  .contact-office { top: 215px; }
  .contact-mobile { top: 252px; }
  .contact-email { top: 304px; font-size: 30px; font-weight: 300; letter-spacing: 0.5px; }
  .contact-email .at { color: var(--cyan-soft); }
  .contact-web { top: 352px; font-size: 27px; font-weight: 600; letter-spacing: 2px; }

  .tagline {
    position: absolute;
    left: 440px; top: 785px; width: 672px;
    text-align: center;
    font-size: 33px; font-weight: 400; line-height: 40px; letter-spacing: 1.5px;
    white-space: nowrap;
  }

  .side-label {
    position: absolute;
    font-family: "Roboto Condensed", "Arial Narrow", sans-serif;
    font-style: italic;
    font-size: 30px;
    color: var(--label-ink);
  }
</style>
</head>
<body>
  <!-- Front side -->
  <div class="card-frame card-front"><div class="card-face"></div></div>
  <div class="brand-mark" style="left:76px; top:66px; width:278px; height:278px;"></div>
  <div class="brand-name" style="left:76px; top:358px; font-size:66px; letter-spacing:3px;">VELTRA</div>

  <div class="rule rule-cyan-to-navy" style="left:405px; top:70px; width:328px;"></div>
  <div class="contact contact-name">JOHN SMITH</div>
  <div class="contact contact-street">123 Fake Street</div>
  <div class="contact contact-phone contact-office"><span class="phone-tag">ph:</span>555-555-5555</div>
  <div class="contact contact-phone contact-mobile"><span class="phone-tag">c:</span>555-555-5555</div>
  <div class="contact contact-email">jsmith<span class="at">@</span>veltra.com</div>
  <div class="contact contact-web">www.veltra.com</div>
  <div class="rule rule-cyan-to-navy" style="left:405px; top:409px; width:328px;"></div>

  <div class="side-label" style="left:818px; top:213px;">FRONT</div>

  <!-- Back side -->
  <div class="card-frame card-back"><div class="card-face"></div></div>
  <div class="brand-mark" style="left:456px; top:582px; width:130px; height:130px;"></div>
  <div class="brand-name" style="left:612px; top:596px; font-size:118px; letter-spacing:2px;">VELTRA</div>

  <div class="rule rule-navy-to-cyan" style="left:452px; top:758px; width:648px;"></div>
  <p class="tagline">Professionals in Kavra, Lumo and<br>Orbitex development and consulting.</p>
  <div class="rule rule-cyan-to-navy" style="left:452px; top:885px; width:648px;"></div>

  <div class="side-label" style="left:258px; top:758px;">BACK</div>
</body>
</html>
```